KTR Business Cards

We require business cards for our business. We would like a matte black back to the card, with our logo centred in the middle. The front side of the card is open to design.

Target Market(s)

Clients looking for legal services (professional)

Industry/Entity Type

Legal

Contact Information for Business Card

Dario Velkenor
Partner
Mobile: 0471 386 524
Email: dario@ktrlaw.co
Website: www.ktrlaw.co
Level 3, 118 Pembury Street
Sydney NSW 2000

Font styles to use
Other font styles liked:
• Avenir

Colors
f04a50
ffffff
1b1b1b

Requirements
Must have
• Black back with logo included in the centre of the card.
• Our font is Avenir.

```html
<!DOCTYPE html>
<html lang="en">
<head>
<meta charset="utf-8">
<title>KTR Legal – Business Cards</title>
<link rel="stylesheet" href="https://fonts.googleapis.com/css2?family=Mulish:wght@400;600;800&display=swap">
<style>
  :root {
    --bg: #1a1a1a;
    --card: #1f1f1f;
    --accent: #c0294a;
    --white: #ffffff;
    --text: #f2f2f2;
  }
  * { margin: 0; padding: 0; box-sizing: border-box; }
  html, body {
    width: 1200px; height: 1000px; overflow: hidden;
    background: var(--bg);
    font-family: "Mulish", "Avenir", sans-serif;
  }
  .canvas { position: relative; width: 1200px; height: 1000px; }
  .card {
    position: absolute;
    width: 517px; height: 296px;
    background: var(--card);
    overflow: hidden;
  }
  .card--front { left: 348px; top: 189px; }
  .card--back  { left: 346px; top: 530px; }

  .holder { position: absolute; left: 35px; top: 24px; }
  .holder__name {
    color: var(--accent); font-weight: 800; font-size: 27px;
    letter-spacing: 0.3px; line-height: 1;
  }
  .holder__role {
    color: var(--text); font-weight: 600; font-size: 17px;
    margin-top: 6px; letter-spacing: 0.3px;
  }
  .corner-shapes { position: absolute; left: 0; top: 0; }

  .address {
    position: absolute; left: 267px; top: 97px;
    color: var(--text); font-size: 16px; font-weight: 600;
    line-height: 23px; letter-spacing: 0.4px; text-transform: uppercase;
  }
  .contacts {
    position: absolute; left: 267px; top: 184px;
    list-style: none; color: var(--text);
    font-size: 16px; font-weight: 600; letter-spacing: 0.4px;
    text-transform: uppercase;
  }
  .contacts__item { display: flex; align-items: center; height: 29px; }
  .contacts__icon { width: 18px; height: 18px; margin-right: 11px; flex: none; }

  .brand {
    position: absolute; inset: 0;
    display: flex; align-items: center; justify-content: center; gap: 20px;
  }
  .brand__mark { width: 34px; height: 34px; background: var(--accent); }
  .brand__name {
    color: var(--white); font-weight: 800; font-size: 48px;
    letter-spacing: 1px; line-height: 1;
  }
</style>
</head>
<body>
<main class="canvas">
  <section class="card card--front" aria-label="Business card front">
    <div class="holder">
      <p class="holder__name">DARIO VELKENOR</p>
      <p class="holder__role">PARTNER</p>
    </div>
    <svg class="corner-shapes" width="200" height="296" viewBox="0 0 200 296" aria-hidden="true">
      <polygon points="0,103 94,196 0,292" fill="var(--white)"/>
      <polygon points="10,296 99,206 189,296" fill="var(--accent)"/>
    </svg>
    <address class="address">
      Level 3,<br>118 Pembury Street<br>Sydney NSW 2000
    </address>
    <ul class="contacts">
      <li class="contacts__item">
        <svg class="contacts__icon" viewBox="0 0 18 18" aria-hidden="true">
          <rect x="4" y="0.5" width="10" height="17" rx="1.5" fill="none" stroke="var(--accent)" stroke-width="1.6"/>
          <line x1="7" y1="14.5" x2="11" y2="14.5" stroke="var(--accent)" stroke-width="1.4"/>
        </svg>0471 386 524</li>
      <li class="contacts__item">
        <svg class="contacts__icon" viewBox="0 0 18 18" aria-hidden="true">
          <rect x="0.5" y="3" width="17" height="12" fill="var(--accent)"/>
          <polyline points="0.5,3 9,10 17.5,3" fill="none" stroke="var(--card)" stroke-width="1.4"/>
        </svg>dario@ktrlaw.co</li>
      <li class="contacts__item">
        <svg class="contacts__icon" viewBox="0 0 18 18" aria-hidden="true">
          <g fill="none" stroke="var(--accent)" stroke-width="1.4">
            <circle cx="9" cy="9" r="7.5"/>
            <ellipse cx="9" cy="9" rx="3.2" ry="7.5"/>
            <line x1="1.5" y1="9" x2="16.5" y2="9"/>
            <line x1="9" y1="1.5" x2="9" y2="16.5"/>
          </g>
        </svg>www.ktrlaw.co</li>
    </ul>
  </section>

  <section class="card card--back" aria-label="Business card back">
    <div class="brand">
      <span class="brand__mark" aria-hidden="true"></span>
      <span class="brand__name">KTR LEGAL</span>
    </div>
  </section>
</main>
</body>
</html>
```